Real Estate "For Sale" Sign for a Colorado Real Estate Company

I need a sign for my Real Estate Company and the size needs to be 24inches by 24inches when printed on metal.
Logo is attached and would like to keep it modern and simple. We are a small town and I am not looking for a new age, industrial design. The concept needs to have the following attributes:

- Logo placed on sign
- Text "For Sale"
- Text "Reid Calloway" and my phone number "720-555-0143" (I would need any font package you use so that I can edit my number if that changes)
- Text "www.reid-calloway.example"
Im open to other attributes as well!

Target Market(s)

General Public driving around town.

Industry/Entity Type

Real Estate Agent

Requirements
Must have
• Logo and the colors must not be too busy. Contact Info very clear.

```html
<!DOCTYPE html>
<html lang="en">
<head>
<meta charset="utf-8">
<title>For Sale Sign – Aldermoor Realty</title>
<link href="https://fonts.googleapis.com/css2?family=Barlow:wght@600;700&display=swap" rel="stylesheet">
<style>
  :root {
    --sky-blue: #1c82c4;
    --navy: #15466a;
    --paper: #f3f3f3;
    --paper-shade: #e6e6e6;
    --white: #ffffff;
  }
  * { margin: 0; padding: 0; box-sizing: border-box; }
  html, body { width: 1200px; height: 1200px; overflow: hidden; background: var(--white); }
  .sign {
    position: relative;
    width: 1200px;
    height: 1200px;
    overflow: hidden;
    font-family: "Barlow", Arial, sans-serif;
    background: var(--sky-blue);
  }
  .sign__backdrop { position: absolute; inset: 0; width: 1200px; height: 1200px; }
  .brand {
    position: absolute;
    left: 88px;
    top: 168px;
    display: flex;
    align-items: center;
    gap: 16px;
    color: var(--navy);
    font-weight: 700;
    font-size: 46px;
    letter-spacing: 1px;
    white-space: nowrap;
  }
  .brand__mark { width: 34px; height: 34px; background: var(--sky-blue); }
  .badge-title {
    position: absolute;
    left: 652px;
    width: 400px;
    text-align: center;
    color: var(--navy);
    font-weight: 700;
    font-size: 172px;
    line-height: 1;
  }
  .badge-title--for { top: 282px; }
  .badge-title--sale { top: 458px; }
  .agent {
    position: absolute;
    left: 52px;
    color: var(--white);
    font-weight: 600;
    line-height: 1;
    white-space: nowrap;
  }
  .agent__name { top: 684px; font-size: 74px; letter-spacing: 1px; }
  .agent__phone { top: 780px; font-size: 80px; letter-spacing: 1px; }
  .website {
    position: absolute;
    left: 0;
    width: 1200px;
    top: 1094px;
    text-align: center;
    color: var(--navy);
    font-weight: 700;
    font-size: 52px;
    line-height: 1;
    white-space: nowrap;
  }
</style>
</head>
<body>
<div class="sign">
  <svg class="sign__backdrop" viewBox="0 0 1500 1500" aria-hidden="true">
    <defs>
      <linearGradient id="paperTone" x1="0" y1="0" x2="1" y2="1">
        <stop offset="0" stop-color="#f3f3f3"/>
        <stop offset="0.5" stop-color="#fafafa"/>
        <stop offset="1" stop-color="#e6e6e6"/>
      </linearGradient>
    </defs>
    <path class="paper-field" fill="url(#paperTone)"
      d="M0 0 H1500 V505 C1200 440 900 440 700 480 C500 530 370 600 260 603 C150 603 50 575 0 545 Z"/>
    <path class="swoosh" fill="var(--navy)"
      d="M0 380 C40 480 120 560 270 592 C150 592 50 560 0 528 Z"/>
    <path class="swoosh" fill="var(--navy)"
      d="M1290 325 C1360 315 1440 310 1500 312 V440 C1450 420 1400 405 1362 400 Z"/>

    <g class="badge" transform="translate(1065 625)" fill="var(--white)" style="filter: drop-shadow(0 4px 6px rgba(0,0,0,0.18));">
      <clipPath id="badgeReach"><circle r="375"/></clipPath>
      <g clip-path="url(#badgeReach)">
        <circle r="348"/>
        <g class="badge-points">
          <rect x="-265" y="-265" width="530" height="530" transform="rotate(0)"/>
          <rect x="-265" y="-265" width="530" height="530" transform="rotate(11.25)"/>
          <rect x="-265" y="-265" width="530" height="530" transform="rotate(22.5)"/>
          <rect x="-265" y="-265" width="530" height="530" transform="rotate(33.75)"/>
          <rect x="-265" y="-265" width="530" height="530" transform="rotate(45)"/>
          <rect x="-265" y="-265" width="530" height="530" transform="rotate(56.25)"/>
          <rect x="-265" y="-265" width="530" height="530" transform="rotate(67.5)"/>
          <rect x="-265" y="-265" width="530" height="530" transform="rotate(78.75)"/>
        </g>
      </g>
    </g>
    <circle cx="1065" cy="625" r="328" fill="none" stroke="var(--navy)" stroke-width="4" stroke-dasharray="10 7"/>
    <g class="badge-rules" stroke="var(--navy)" stroke-width="2.5">
      <line x1="818" y1="803" x2="1310" y2="803"/>
      <line x1="862" y1="830" x2="1268" y2="830"/>
      <line x1="905" y1="857" x2="1225" y2="857"/>
      <line x1="948" y1="883" x2="1182" y2="883"/>
      <line x1="992" y1="910" x2="1138" y2="910"/>
    </g>

    <polygon class="ribbon-end" fill="var(--navy)" points="0,1362 215,1362 175,1404 215,1446 0,1446"/>
    <polygon class="ribbon-end" fill="var(--navy)" points="1285,1362 1500,1362 1500,1446 1285,1446 1325,1404"/>
  </svg>

  <div class="brand">
    <span class="brand__mark"></span>
    <span class="brand__name">ALDERMOOR REALTY LLC</span>
  </div>

  <div class="badge-title badge-title--for">FOR</div>
  <div class="badge-title badge-title--sale">SALE</div>

  <div class="agent agent__name">REID CALLOWAY</div>
  <div class="agent agent__phone">720-555-0143</div>

  <div class="website">WWW.REID-CALLOWAY.EXAMPLE</div>
</div>
</body>
</html>
```